Truck Wrap Design

Project Scope
Design a full vehicle wrap for a box truck (Pantech-style) that elevates the brand identity of Larkfield Signs and Wraps. The design should reflect the fun, approachable personality of the brand while delivering a bold and professional visual impact that turns heads in traffic.
⸻
Design Goals
• Maintain the character-driven style shown in the initial mockup (squeegee mascot with a heat gun).
• Preserve the brand colour palette (deep navy, magenta, teal blue).
• Use a wavy, flowing background as seen in the mockup — but refine it with more defined lines or structured layering, inspired by BrightMarrow’s confident composition.
• Ensure high visibility of the brand name and contact number from a distance.
• Vehicle should be recognisable and consistent with other brand assets (uniforms, cards, hats).
• Create front, side, and rear panel views.
⸻
Creative Style & Tone
• Playful but sharp.
• Friendly and energetic with a hint of retro charm (like BrightMarrow’s Tidewell Co and Snug Otter).
• Character-forward branding (the mascot should have presence and personality, not be lost in background noise).
⸻
Design Elements to Include
• Logo – prominent on all sides
•. Mascot – showcased clearly, ideally interacting with the background or layout
• Phone number – clearly legible and consistently placed
• Slogan or service callout (optional) – such as “Vehicle Wraps, LED Signs & More”
• Website URL – small but readable near rear or base panel
• Colours – Stick to current palette: Navy, Magenta, Teal, White
• Flowing background – evolve current wave style with sharper edges or layered “ribbons”
• Typography – Clean, bold fonts. Avoid thin script or overly quirky type.
⸻
Avoid
• Overcrowding the design with too many service listings
• Heavy gradients that muddy the clarity from afar
• Muted colours — we want contrast and pop

```html
<!DOCTYPE html>
<html lang="en">
<head>
<meta charset="utf-8">
<title>Larkfield Signs and Wraps – Box Truck Wrap Panels</title>
<link rel="stylesheet" href="https://fonts.googleapis.com/css2?family=Poppins:wght@700;800&display=swap">
<style>
  :root {
    --teal: #3aaed3;
    --teal-light: #5cc3e3;
    --magenta: #d6317a;
    --magenta-deep: #b81f66;
    --navy: #1f3a4f;
    --navy-deep: #172d3e;
    --white: #ffffff;
    --stage: #e9ecef;
  }
  * { box-sizing: border-box; margin: 0; padding: 0; }
  html, body { width: 765px; height: 1200px; overflow: hidden; }
  body {
    background: var(--stage);
    font-family: "Poppins", sans-serif;
    display: flex;
    flex-direction: column;
    justify-content: center;
    align-items: center;
    gap: 90px;
  }
  .truck-side {
    display: flex;
    align-items: flex-end;
    gap: 15px;
  }
  .panel-bg { position: absolute; inset: 0; width: 100%; height: 100%; }

  /* Box panel */
  .box-panel {
    position: relative;
    width: 540px;
    height: 258px;
    overflow: hidden;
    background: var(--teal);
  }
  .contact {
    position: absolute;
    top: 40px;
    color: var(--magenta-deep);
    font-weight: 800;
    line-height: 1;
    white-space: nowrap;
  }
  .contact__phone { font-size: 30px; letter-spacing: 0.3px; }
  .contact__url { color: var(--white); font-weight: 700; font-size: 14px; margin-top: 4px; }
  .truck-side--driver .contact { left: 30px; transform: rotate(-8deg); transform-origin: left center; }
  .truck-side--passenger .contact { right: 30px; transform: rotate(8deg); transform-origin: right center; }

  .brand-name {
    position: absolute;
    color: var(--white);
    font-weight: 800;
    line-height: 1;
    white-space: nowrap;
  }
  .brand-name__main { display: block; font-size: 54px; letter-spacing: -1px; }
  .brand-name__sub { display: block; font-size: 17px; letter-spacing: 1.2px; text-transform: uppercase; margin-top: 6px; padding-left: 4px; }
  .truck-side--driver .brand-name { left: 30px; top: 118px; }
  .truck-side--passenger .brand-name { left: 240px; top: 128px; }

  .mascot {
    position: absolute;
    width: 125px;
    height: 205px;
    top: 18px;
    border-radius: 16px;
    background: linear-gradient(160deg, var(--teal-light), var(--teal) 60%, var(--navy));
  }
  .truck-side--driver .mascot { left: 318px; }
  .truck-side--passenger .mascot { left: 100px; }

  .services {
    position: absolute;
    bottom: 18px;
    color: var(--white);
    font-weight: 700;
    font-size: 14px;
    line-height: 1.3;
    list-style: none;
  }
  .truck-side--driver .services { right: 14px; text-align: left; }
  .truck-side--passenger .services { left: 14px; text-align: right; }

  /* Cab door panel */
  .cab-panel {
    position: relative;
    width: 150px;
    height: 160px;
    overflow: hidden;
    background: var(--teal);
    border-radius: 10px 10px 4px 4px;
  }
  .cab-brand {
    position: absolute;
    top: 112px;
    color: var(--white);
    font-weight: 800;
    line-height: 1;
    white-space: nowrap;
  }
  .cab-brand__main { display: block; font-size: 19px; letter-spacing: -0.3px; }
  .cab-brand__sub { display: block; font-size: 6.5px; letter-spacing: 0.6px; text-transform: uppercase; margin-top: 3px; padding-left: 2px; }
  .truck-side--driver .cab-brand { left: 40px; }
  .truck-side--passenger .cab-brand { right: 18px; }
</style>
</head>
<body>

<section class="truck-side truck-side--driver" aria-label="Driver side">
  <div class="cab-panel" aria-label="Driver cab door">
    <svg class="panel-bg" viewBox="0 0 150 160" preserveAspectRatio="none" aria-hidden="true">
      <rect width="150" height="160" fill="var(--teal)"/>
      <polygon points="0,110 150,78 150,106 0,138" fill="var(--magenta)"/>
      <polygon points="0,138 150,106 150,160 0,160" fill="var(--navy)"/>
    </svg>
    <div class="cab-brand">
      <span class="cab-brand__main">Larkfield</span>
      <span class="cab-brand__sub">Signs and Wraps</span>
    </div>
  </div>
  <div class="box-panel" aria-label="Driver side box panel">
    <svg class="panel-bg" viewBox="0 0 540 258" preserveAspectRatio="none" aria-hidden="true">
      <rect width="540" height="258" fill="var(--teal)"/>
      <polygon points="0,168 540,62 540,92 0,198" fill="var(--magenta)"/>
      <polygon points="0,198 540,92 540,258 0,258" fill="var(--navy)"/>
      <polygon points="0,240 540,150 540,258 0,258" fill="var(--navy-deep)" opacity="0.5"/>
    </svg>
    <div class="contact">
      <div class="contact__phone">123-555-0147</div>
      <div class="contact__url">www.larkfieldsigns.com</div>
    </div>
    <div class="brand-name">
      <span class="brand-name__main">Larkfield</span>
      <span class="brand-name__sub">Signs and Wraps</span>
    </div>
    <div class="mascot" role="img" aria-label="Squeegee mascot character holding a heat gun"></div>
    <ul class="services">
      <li>Vehicle Wraps</li>
      <li>LED Signs</li>
      <li>&amp; More</li>
    </ul>
  </div>
</section>

<section class="truck-side truck-side--passenger" aria-label="Passenger side">
  <div class="box-panel" aria-label="Passenger side box panel">
    <svg class="panel-bg" viewBox="0 0 540 258" preserveAspectRatio="none" aria-hidden="true">
      <rect width="540" height="258" fill="var(--teal)"/>
      <polygon points="0,62 540,168 540,198 0,92" fill="var(--magenta)"/>
      <polygon points="0,92 540,198 540,258 0,258" fill="var(--navy)"/>
      <polygon points="0,150 540,240 540,258 0,258" fill="var(--navy-deep)" opacity="0.5"/>
    </svg>
    <div class="contact">
      <div class="contact__phone">123-555-0147</div>
      <div class="contact__url">www.larkfieldsigns.com</div>
    </div>
    <div class="brand-name">
      <span class="brand-name__main">Larkfield</span>
      <span class="brand-name__sub">Signs and Wraps</span>
    </div>
    <div class="mascot" role="img" aria-label="Squeegee mascot character holding a heat gun"></div>
    <ul class="services">
      <li>Vehicle Wraps</li>
      <li>LED Signs</li>
      <li>&amp; More</li>
    </ul>
  </div>
  <div class="cab-panel" aria-label="Passenger cab door">
    <svg class="panel-bg" viewBox="0 0 150 160" preserveAspectRatio="none" aria-hidden="true">
      <rect width="150" height="160" fill="var(--teal)"/>
      <polygon points="0,78 150,110 150,138 0,106" fill="var(--magenta)"/>
      <polygon points="0,106 150,138 150,160 0,160" fill="var(--navy)"/>
    </svg>
    <div class="cab-brand">
      <span class="cab-brand__main">Larkfield</span>
      <span class="cab-brand__sub">Signs and Wraps</span>
    </div>
  </div>
</section>

</body>
</html>
```